Lumen! Consulting

We need a web design for a new supply chain consulting business. we will work with major brands in the electronics, apparel, toy and jewelry industries to create a sustainability program for our customers and implement in their supply chain. We want our customers to have confidence in their supply chain responsibility program. We also manage stakeholder engagements, NGO relationships, and external communications.

I would like to colors to be green, orange and/or black to match the logo (attached). The final design should communicate positive and optimistic leadership - for a professional, sustainable, business.

Industry/Entity Type

Business

```html
<!DOCTYPE html>
<html lang="en">
<head>
<meta charset="utf-8">
<title>Lumen! Consulting</title>
<link href="https://fonts.googleapis.com/css2?family=Oswald:wght@300;400&family=Arimo:wght@400;700&display=swap" rel="stylesheet">
<style>
:root{
  --orange:#f7a02a;
  --green:#8cc63f;
  --green-dark:#6ea82c;
  --ink:#555;
  --dark:#3a3a3a;
  --muted:#8a8a8a;
  --band:#efefef;
}
*{margin:0;padding:0;box-sizing:border-box}
html,body{width:922px;height:1200px;overflow:hidden;background:#fff}
body{position:relative;font-family:"Arimo",Arial,sans-serif;color:var(--ink);font-size:10.5px}
.abs{position:absolute}
.head{font-family:"Oswald",sans-serif;font-weight:400;color:var(--orange)}
/* header */
.brand{left:76px;top:20px;display:flex;align-items:center;gap:8px}
.brand .dot{width:30px;height:30px;border-radius:50%;background:var(--green)}
.brand span{font-family:"Oswald",sans-serif;font-size:30px;color:var(--orange);font-weight:300}
.nav{left:313px;top:50px;display:flex}
.nav a{font-family:"Oswald",sans-serif;font-weight:300;font-size:15px;color:var(--muted);text-decoration:none;margin-right:35px}
.nav a.active{color:var(--orange)}
.rule{left:0;top:102px;width:922px;height:4px;background:var(--orange)}
/* hero */
.hero{left:0;top:106px;width:922px;height:239px;background:linear-gradient(90deg,#8e8e8e,#a9a9a9 60%,#b5b5b5)}
.hero h1{left:68px;top:48px;width:300px;font-size:19px;line-height:26px;letter-spacing:.5px}
.hero p{left:68px;top:106px;width:270px;font-size:11px;line-height:17.6px;color:#fff}
.hero .product{left:395px;top:4px;width:465px;height:235px;background:linear-gradient(135deg,#e6e6e6,#cfcfcf 45%,#3d3d3d 46%,#5a5a5a 70%,#dcdcdc);border-radius:6px}
/* welcome */
.welcome{left:0;top:352px;width:922px;text-align:center;font-size:19.5px}
.team{left:59px;top:388px;width:376px;height:187px;background:linear-gradient(120deg,#2b2b2b,#8a7b70 45%,#e9e7e3 70%,#3a3a3a)}
.intro{left:445px;top:384px;width:400px;font-size:10.3px;line-height:17.6px}
.intro p+p{margin-top:17.6px}
/* features */
.band{left:0;top:595px;width:922px;height:240px;background:var(--band)}
.feature{top:8px;width:250px;text-align:center}
.feature .ico{width:88px;height:88px;border-radius:50%;background:#fff;margin:0 auto;display:flex;align-items:center;justify-content:center}
.feature h2{font-size:19.5px;margin-top:8px}
.feature p{text-align:left;font-size:10.3px;line-height:17.6px;margin-top:2px;padding-left:6px}
.btn{display:inline-block;margin-top:7px;width:86px;height:28px;background:var(--green);border-bottom:3px solid var(--green-dark);color:#fff;font-family:"Oswald",sans-serif;font-size:14.5px;line-height:25px;font-weight:300}
/* news / testimonials */
.sec-title{font-size:19.5px}
.news{left:66px;top:838px;width:386px}
.news .item{border-bottom:1px dotted #b9d98e;padding:6px 0 5px}
.news h3{font-size:11.3px;color:#444;font-weight:700}
.news p{font-size:10.3px;line-height:13.6px;margin-top:5px;padding-right:8px}
.news .more{display:block;text-align:right;color:var(--orange);font-family:"Oswald",sans-serif;font-weight:300;font-size:13px;text-decoration:underline;margin-top:-2px}
.clients{left:470px;top:838px;width:378px}
.quote{position:relative;height:68px;display:flex;gap:6px;border-bottom:1px dotted #b9d98e;padding:6px 0 0 4px}
.quote + .quote{margin-top:0}
.quote .pic{flex:none;width:56px;height:56px;background:linear-gradient(#e8e2d8,#c7b193)}
.quote p{font-size:10.3px;line-height:13.6px;color:#555;padding-left:20px;padding-right:4px;position:relative}
.quote p::before{content:"\201C";position:absolute;left:2px;top:-4px;font-size:26px;color:#999;font-family:Georgia,serif}
.quote .who{position:absolute;right:2px;bottom:5px;font-size:10.3px;color:var(--orange)}
/* footer */
.foot{left:0;top:1012px;width:922px;height:161px;background:var(--dark)}
.foot .links{left:69px;top:8px}
.foot .links a{display:block;font-family:"Oswald",sans-serif;font-weight:300;font-size:13.5px;color:#fff;text-decoration:none;line-height:21.6px}
.foot .links a:first-child{color:var(--orange)}
.foot h4{font-size:19.5px}
.foot .col p{color:#eee;font-size:10.3px;line-height:17.6px;margin-top:2px}
.social{left:675px;top:44px;width:170px;display:grid;grid-template-columns:repeat(4,30px);gap:17px 15px}
.social span{width:30px;height:30px;border-radius:50%;background:var(--orange);border:2px solid #fff;display:flex;align-items:center;justify-content:center}
.copy{left:0;top:1178px;width:922px;text-align:center;font-size:10px;color:#333}
.copy a{color:var(--orange);text-decoration:underline}
</style>
</head>
<body>
<header>
  <div class="abs brand"><i class="dot"></i><span>Lumen!</span></div>
  <nav class="abs nav">
    <a class="active" href="#">Home</a><a href="#">Blog</a><a href="#">Clients</a><a href="#">Capabilities</a><a href="#">Industries</a><a href="#">Experience</a><a href="#" style="margin-right:0">Contact</a>
  </nav>
  <div class="abs rule"></div>
</header>

<section class="abs hero">
  <h1 class="abs head">Lorem Ipsum is simply dummy text of the printing and typesetting .</h1>
  <p class="abs">Lorem Ipsum is simply dummy text of the printing and typesetting industry. Lorem Ipsum has been the industry's standard dummy text ever since the 1500s</p>
  <div class="abs product" role="img" aria-label="Product photo: camera bag, mirrorless camera, lens and two smartphones"></div>
</section>

<h2 class="abs head welcome">Welcome to LUMEN Supply Chain Management</h2>
<div class="abs team" role="img" aria-label="Photo of business team reviewing documents at a meeting"></div>
<div class="abs intro">
  <p>Lorem Ipsum is simply dummy text of the printing and typesetting industry. Lorem Ipsum has been the industry's standard dummy text ever since the 1500s, when an unknown printer took a galley of type and scrambled it to make a type specimen book. It has survived not only five centuries, but also the leap into electronic typesetting, remaining essentially unchanged. It was popularised in the 1960s with the release of Letraset sheets containing Lorem Ipsum passages, and more recently with desktop publishing software like Aldus PageMaker including versions of Lorem Ipsum.</p>
  <p>Lorem Ipsum is simply dummy text of the printing and typesetting industry. Lorem Ipsum has been the industry's standard dummy text ever since the 1500s, when an unknown printer took a galley of type and scrambled it to make a type specimen book.</p>
</div>

<section class="abs band">
  <div class="abs feature" style="left:64px">
    <div class="ico"><svg width="40" height="56" viewBox="0 0 40 56"><path d="M20 4a15 15 0 0 0-9 27c2 2 3 4 3 7h12c0-3 1-5 3-7A15 15 0 0 0 20 4z" fill="none" stroke="#8cc63f" stroke-width="5"/><rect x="13" y="41" width="14" height="4" fill="#8cc63f"/><rect x="14" y="47" width="12" height="4" fill="#8cc63f"/></svg></div>
    <h2 class="head">Challange</h2>
    <p>Lorem Ipsum is simply dummy text of the printing and typesetting industry. Lorem Ipsum has been the industry's standard dummy text ever since the 1500s, when an unknown printer took a galley of type...</p>
    <span class="btn">Read More</span>
  </div>
  <div class="abs feature" style="left:333px">
    <div class="ico"><svg width="40" height="52" viewBox="0 0 40 52"><rect x="3" y="3" width="34" height="46" fill="none" stroke="#f7a02a" stroke-width="3"/><g fill="#f7a02a"><rect x="9" y="9" width="5" height="4"/><rect x="17" y="9" width="5" height="4"/><rect x="25" y="9" width="5" height="4"/><rect x="9" y="17" width="5" height="4"/><rect x="17" y="17" width="5" height="4"/><rect x="25" y="17" width="5" height="4"/><rect x="9" y="25" width="5" height="4"/><rect x="17" y="25" width="5" height="4"/><rect x="25" y="25" width="5" height="4"/><rect x="15" y="37" width="10" height="12"/></g></svg></div>
    <h2 class="head">Industry</h2>
    <p>Lorem Ipsum is simply dummy text of the printing and typesetting industry. Lorem Ipsum has been the industry's standard dummy text ever since the 1500s, when an unknown printer took a galley of type...</p>
    <span class="btn">Read More</span>
  </div>
  <div class="abs feature" style="left:605px">
    <div class="ico"><svg width="62" height="44" viewBox="0 0 62 44"><path d="M6 40C6 14 30 2 58 4 56 30 36 42 12 36" fill="#8cc63f"/><path d="M4 42C18 28 32 20 46 14" stroke="#fff" stroke-width="3" fill="none"/></svg></div>
    <h2 class="head">Expertise</h2>
    <p>Lorem Ipsum is simply dummy text of the printing and typesetting industry. Lorem Ipsum has been the industry's standard dummy text ever since the 1500s, when an unknown printer took a galley of type...</p>
    <span class="btn">Read More</span>
  </div>
</section>

<section class="abs news">
  <h2 class="head sec-title">Latest News</h2>
  <div class="item">
    <h3>Lorem Ipsum is simply dummy text of the printing industry.</h3>
    <p>Lorem Ipsum is simply dummy text of the printing and typesetting industry. Lorem Ipsum has been the industry's standard dummy text ever since the 1500s...</p>
    <a class="more" href="#">Read More</a>
  </div>
  <div class="item">
    <h3>Lorem Ipsum is simply dummy text of the printing industry.</h3>
    <p>Lorem Ipsum is simply dummy text of the printing and typesetting industry. Lorem Ipsum has been the industry's standard dummy text ever since the 1500s...</p>
    <a class="more" href="#">Read More</a>
  </div>
</section>

<section class="abs clients">
  <h2 class="head sec-title">Client Speak</h2>
  <div class="quote">
    <div class="pic" role="img" aria-label="Client portrait photo"></div>
    <p>Lorem Ipsum is simply dummy text of the printing and typesetting industry. Lorem Ipsum has been the industry's standard dummy text ever since the 1500s, when an unknown printer took galley...&rdquo;</p>
    <span class="who">- Client Name</span>
  </div>
  <div class="quote">
    <div class="pic" role="img" aria-label="Client portrait photo"></div>
    <p>Lorem Ipsum is simply dummy text of the printing and typesetting industry. Lorem Ipsum has been the industry's standard dummy text ever since the 1500s, when an unknown printer took galley...&rdquo;</p>
    <span class="who">- Client Name</span>
  </div>
</section>

<footer class="abs foot">
  <nav class="abs links">
    <a href="#">Home</a><a href="#">About</a><a href="#">Clients</a><a href="#">Capabilities</a><a href="#">Industries</a><a href="#">Experience</a><a href="#">Contact</a>
  </nav>
  <div class="abs col" style="left:265px;top:6px;width:190px">
    <h4 class="head">How can we help</h4>
    <p>Lorem Ipsum is simply dummy text of the printing and typesetting industry. Lorem Ipsum has been the industry's standard dummy text ever since 1500s</p>
    <p style="margin-top:17.6px">Lorem Ipsum is simply dummy text of the printing and typesetting industry.</p>
  </div>
  <div class="abs col" style="left:471px;top:6px;width:195px">
    <h4 class="head">Get in Touch With Us</h4>
    <p>Office no., Area name<br>City, State, Country<br>Call : +44 100 200 3000<br>Fax : +44 100 200 3000<br>Email : info@lumenconsult.com<br>Support : support@lumenconsult.com</p>
  </div>
  <h4 class="abs head" style="left:672px;top:6px">Follow Us</h4>
  <div class="abs social" aria-label="Social media links">
    <span><svg width="14" height="14" viewBox="0 0 14 14"><g fill="#fff"><circle cx="3" cy="7" r="2.2"/><circle cx="11" cy="3" r="2.2"/><circle cx="11" cy="11" r="2.2"/></g><path d="M3 7L11 3M3 7l8 4" stroke="#fff" stroke-width="1.3"/></svg></span>
    <span><svg width="14" height="14" viewBox="0 0 14 14"><g fill="#fff"><circle cx="3" cy="7" r="2.2"/><circle cx="11" cy="3" r="2.2"/><circle cx="11" cy="11" r="2.2"/></g><path d="M3 7L11 3M3 7l8 4" stroke="#fff" stroke-width="1.3"/></svg></span>
    <span><svg width="14" height="14" viewBox="0 0 14 14"><g fill="#fff"><circle cx="3" cy="7" r="2.2"/><circle cx="11" cy="3" r="2.2"/><circle cx="11" cy="11" r="2.2"/></g><path d="M3 7L11 3M3 7l8 4" stroke="#fff" stroke-width="1.3"/></svg></span>
    <span><svg width="14" height="14" viewBox="0 0 14 14"><g fill="#fff"><circle cx="3" cy="7" r="2.2"/><circle cx="11" cy="3" r="2.2"/><circle cx="11" cy="11" r="2.2"/></g><path d="M3 7L11 3M3 7l8 4" stroke="#fff" stroke-width="1.3"/></svg></span>
    <span><svg width="14" height="14" viewBox="0 0 14 14"><g fill="#fff"><circle cx="3" cy="7" r="2.2"/><circle cx="11" cy="3" r="2.2"/><circle cx="11" cy="11" r="2.2"/></g><path d="M3 7L11 3M3 7l8 4" stroke="#fff" stroke-width="1.3"/></svg></span>
    <span><svg width="14" height="14" viewBox="0 0 14 14"><g fill="#fff"><circle cx="3" cy="7" r="2.2"/><circle cx="11" cy="3" r="2.2"/><circle cx="11" cy="11" r="2.2"/></g><path d="M3 7L11 3M3 7l8 4" stroke="#fff" stroke-width="1.3"/></svg></span>
    <span><svg width="14" height="14" viewBox="0 0 14 14"><g fill="#fff"><circle cx="3" cy="7" r="2.2"/><circle cx="11" cy="3" r="2.2"/><circle cx="11" cy="11" r="2.2"/></g><path d="M3 7L11 3M3 7l8 4" stroke="#fff" stroke-width="1.3"/></svg></span>
    <span><svg width="14" height="14" viewBox="0 0 14 14"><g fill="#fff"><circle cx="3" cy="7" r="2.2"/><circle cx="11" cy="3" r="2.2"/><circle cx="11" cy="11" r="2.2"/></g><path d="M3 7L11 3M3 7l8 4" stroke="#fff" stroke-width="1.3"/></svg></span>
  </div>
</footer>
<p class="abs copy">© <a href="#">LUMEN</a> - 2014. All Rights Reserved.</p>
</body>
</html>
```